ESTIV Convention 2025 Quebec City

We would like to have a poster for the promotion and publicity of a convention for ESTIV. The goal is to obtain in A4 format and in US letter format (8.5 X 11) a poster for the upcoming convention in Quebec City.
Here are the 2 images (Maren-8 and Maren-24) that we chose yesterday and that inspire us.

Also the 3 posters of previous Conventions (Revue L+E 252, 261 & 273) As a model of what we are looking for.

As for what should also appear on the poster of the Quebec Convention 2025, here are the main points:

Mandatory at the very top of the poster: ESTIV and the wings (as on the posters of the previous Conventions attached) or at least leave such a space free because I believe that the printers of the High Chapter are redoing this acronym by themselves- same for the review Lys-Étoile.
Then the rest can be left to the imagination of the artists.

Here are the important things that should be included:
Harbor Accord
Quebec city
October 11 and 12, 2025
Light (This is the theme of the convention)
Glow to warm every heart (That's the name of the convention)

Please post it in French and NO RELATION TO RELIGIOUS OR RELIGION!!! :)

The website of the organization for more info if required is: www.lys-etoile-demo.org

If you think of anything else to add, no problem.

Target Market(s)

ESTIV members only

Industry/Entity Type

OSBL - Organisme philosophique ( non religieux )

Font styles to use
Serif
Sans Serif

Requirements
Must have
• ESTIV wings logo
Nice to have
• All in French and without reference to religion, also the GOLD color is appreciated
Should not have
• Of aspect or reference to the religious

```html
<!DOCTYPE html>
<html lang="fr">
<head>
<meta charset="utf-8">
<title>ESTIV – Convention 2025</title>
<link rel="stylesheet" href="https://fonts.googleapis.com/css2?family=Montserrat:wght@400;600;700;800&family=Oswald:wght@600;700&family=Playfair+Display:wght@900&display=swap">
<style>
  :root {
    --page: #ffffff;
    --sky-top: #b4533a;
    --sky-mid: #e9803f;
    --sky-glow: #f7c25a;
    --night: #1a0f0b;
    --ink: #1b120e;
    --title-red: #d9401f;
    --placeholder: #e6a060;
    --gold: #e2b13c;
    --gold-light: #f3d27a;
    --white: #ffffff;
    --rule: #d9cfc6;
  }
  * { box-sizing: border-box; margin: 0; padding: 0; }
  html, body { width: 1200px; height: 2224px; overflow: hidden; background: var(--page); }
  .poster {
    position: absolute; left: 50px; top: 401px; width: 1100px; height: 1421px;
    overflow: hidden; font-family: "Montserrat", sans-serif; color: var(--ink);
    box-shadow: 0 10px 40px rgba(0,0,0,.12);
  }
  .poster-scene {
    position: absolute; inset: 0;
    background:
      radial-gradient(ellipse 22% 9% at 52% 58%, #fff3b0 0%, rgba(255,214,110,.8) 40%, rgba(255,180,80,0) 100%),
      linear-gradient(180deg, var(--sky-top) 0%, #cf6a3f 22%, var(--sky-mid) 42%, var(--sky-glow) 56%, #c4502a 66%, #5a2414 76%, var(--night) 86%, var(--night) 100%);
  }
  .brand { position: absolute; top: 70px; left: 0; right: 0; text-align: center; }
  .brand-name {
    display: inline-flex; align-items: center; gap: 18px;
    font-weight: 700; font-size: 64px; letter-spacing: 14px; color: var(--ink);
  }
  .brand-dot { width: 22px; height: 22px; border-radius: 50%; background: var(--ink); }
  .brand-order { margin-top: 14px; font-size: 32px; font-weight: 400; letter-spacing: 1px; color: #2a1a12; }
  .title { position: absolute; top: 280px; left: 0; right: 0; text-align: center; }
  .title-line { font-size: 62px; font-weight: 400; line-height: 78px; color: var(--ink); letter-spacing: 1px; white-space: nowrap; }
  .title-word {
    margin-top: 12px; display: flex; justify-content: center; align-items: center;
    font-weight: 800; font-size: 200px; line-height: 1; color: var(--title-red); letter-spacing: -2px;
  }
  .title-globe {
    width: 156px; height: 156px; border-radius: 50%; margin: 0 6px;
    background: var(--placeholder);
  }
  .date-band {
    position: absolute; top: 1081px; left: 127px; width: 846px; height: 84px;
    background: linear-gradient(90deg, var(--gold) 0%, var(--gold-light) 50%, var(--gold) 100%);
    clip-path: polygon(0 0, 100% 0, 96% 50%, 100% 100%, 0 100%, 4% 50%);
    display: flex; align-items: center; justify-content: center; gap: 36px;
    font-family: "Oswald", sans-serif; color: var(--ink);
  }
  .date-month { font-family: "Montserrat", sans-serif; font-weight: 800; font-size: 50px; letter-spacing: 2px; }
  .date-days { font-weight: 700; font-size: 76px; letter-spacing: -2px; }
  .date-days small { font-size: 34px; font-family: "Montserrat", sans-serif; font-weight: 800; margin: 0 4px; }
  .date-year { font-weight: 700; font-size: 76px; margin-left: 40px; }
  .footer {
    position: absolute; top: 1200px; left: 100px; right: 50px; height: 170px;
    display: flex; align-items: center; color: var(--white);
  }
  .theme { width: 280px; }
  .theme-name { font-family: "Playfair Display", serif; font-weight: 900; font-size: 56px; line-height: 1; }
  .theme-note { font-size: 22px; line-height: 25px; margin-top: 6px; }
  .divider { width: 2px; height: 100px; background: var(--rule); }
  .footer-mark {
    width: 220px; display: flex; flex-direction: column; align-items: center; gap: 10px;
    font-weight: 700; font-size: 30px; letter-spacing: 4px; color: var(--gold);
  }
  .footer-mark-dot { width: 56px; height: 56px; border-radius: 50%; background: var(--gold); }
  .venue { padding-left: 40px; font-weight: 800; font-size: 27px; line-height: 35px; letter-spacing: 1px; white-space: nowrap; }
  .venue-city { margin-top: 12px; }
</style>
</head>
<body>
  <main class="poster">
    <div class="poster-scene" role="img" aria-label="Coucher de soleil sur un fjord entre deux falaises, avec des oiseaux en vol"></div>

    <header class="brand">
      <div class="brand-name"><span class="brand-dot"></span>ESTIV</div>
      <div class="brand-order">ORDRE DE LA LYS-ÉTOILE</div>
    </header>

    <section class="title">
      <p class="title-line">RAYONNER</p>
      <p class="title-line">POUR RÉCHAUFFER CHAQUE</p>
      <p class="title-word">C<span class="title-globe" role="img" aria-label="Illustration d’un globe terrestre à la place de la lettre O"></span>EUR</p>
    </section>

    <div class="date-band">
      <span class="date-month">OCTOBRE</span>
      <span class="date-days">11<small>et</small>12<span class="date-year">2025</span></span>
    </div>

    <footer class="footer">
      <div class="theme">
        <p class="theme-name">LUMIÈRE</p>
        <p class="theme-note">(C’est le thème de<br>la convention)</p>
      </div>
      <span class="divider"></span>
      <div class="footer-mark"><span class="footer-mark-dot"></span>ESTIV</div>
      <span class="divider"></span>
      <div class="venue">
        <p>ACCORD DU<br>HAVRE</p>
        <p class="venue-city">LA VILLE DE QUÉBEC</p>
      </div>
    </footer>
  </main>
</body>
</html>
```